Design and develop an e-commerce website for Our Home appliances store

Design and develop an e-commerce website for Our home appliances store that sells home appliances such as pots, kettle, plates, dish washer, microwave,
gas cooker, heat extractor etc.
I want any good shopping cart platform such as Bigcommerce, Wordpress, Bigcartel, Woocommerce and others .We want a new template. No need to install it on our website, we will take care of that.

To win the contest please present a sample of:
- the home page
- the product page
- the page where all the items that we sale are listed
- the shopping cart page

I have written some information here for you.

PLEASE READ DESCRIPTION CAREFULLY.

The website i require will have a several areas. Products, which prices that can be added to shopping basket.
I also require the site to have a customer login facility , so that once a customer has used the site they
can login themselves at a later stage and see previous orders and then repeat an order if required.

Must have

Logo must be included.
I would also need to able to manage this site myself, by adding new items and deleting items that are no longer available.

Good luck and for any question please don't hesitate to ask

Store

Coded - Design and coding required

```html
<!DOCTYPE html>
<html lang="en">
<head>
<meta charset="utf-8">
<title>Kitchen Nest – Home Appliances Store</title>
<link href="https://fonts.googleapis.com/css2?family=Raleway:wght@400;500;600;700;800&family=Open+Sans:wght@400;600;700&display=swap" rel="stylesheet">
<style>
:root{
  --orange:#e8501e;
  --dark:#2a2a2a;
  --darker:#222;
  --nav:#333;
  --green:#6cc62c;
  --yellow:#f7d40c;
  --red:#e6262b;
  --hero:#cfe7f6;
  --blue:#3aa9e9;
  --label:#2f3843;
  --text:#333;
  --muted:#888;
  --line:#e3e3e3;
  --cardline:#dfe9f2;
  --price:#e8501e;
  --white:#fff;
}
*{box-sizing:border-box;margin:0;padding:0}
html,body{width:1200px;height:4100px;overflow:hidden}
body{position:relative;background:var(--white);font-family:"Open Sans",Arial,sans-serif;color:var(--text);font-size:12px}
.sec{position:absolute;left:0;width:1200px}
.wrap{position:absolute;left:93px;width:1014px}
h1,h2,h3,h4,.raleway{font-family:"Raleway",Arial,sans-serif}
ul{list-style:none}
.ph{display:block}

/* top bar */
.topbar{top:0;height:26px;background:linear-gradient(90deg,var(--orange) 0 38%,var(--dark) 38% 62%,var(--green) 62% 100%);color:#fff;font-size:10px}
.topbar .left{position:absolute;left:96px;top:7px;display:flex;gap:26px;text-transform:uppercase}
.topbar .right{position:absolute;left:790px;top:7px;display:flex;gap:22px}
.topbar .right span::before{content:"";display:inline-block;width:8px;height:8px;border-radius:50%;background:#fff;margin-right:5px;vertical-align:-1px}

/* header */
.header{top:26px;height:96px;background:var(--dark)}
.logo{position:absolute;left:96px;top:22px;font-family:"Raleway",sans-serif;font-weight:800;font-size:44px;color:var(--green);letter-spacing:1px}
.search{position:absolute;left:660px;top:35px;width:447px;height:30px;background:#3c3c3c;border:1px solid #4a4a4a;color:#999;font-size:11px;padding:7px 12px}
.search svg{position:absolute;right:10px;top:8px}

/* nav */
.nav{top:122px;height:42px;background:var(--nav);border-top:1px solid #444}
.nav ul{position:absolute;left:93px;top:0;display:flex;height:42px}
.nav li{color:#fff;font-family:"Raleway",sans-serif;font-weight:600;font-size:15px;padding:11px 14px;border-right:1px solid #444}
.nav li.active{background:var(--orange)}
.cart{position:absolute;left:930px;top:0;width:177px;height:42px;background:var(--yellow);color:#222;font-weight:700;font-size:13px;padding:12px 14px 0 44px}
.cart svg{position:absolute;left:14px;top:11px}

/* hero */
.hero{top:164px;height:345px;background:var(--hero)}
.hero h1{position:absolute;left:96px;top:80px;font-weight:700;font-size:52px;color:#3a3a3a}
.hero .tag{position:absolute;left:96px;top:156px;width:500px;height:78px;background:var(--red);color:#fff;font-family:"Raleway",sans-serif;font-weight:500;font-size:37px;line-height:74px;padding:0 0 0 16px;border-left:4px solid #fff;white-space:nowrap;overflow:hidden}
.hero .shop{position:absolute;left:96px;top:269px;width:112px;height:32px;background:var(--dark);color:#fff;font-size:13px;text-align:center;padding-top:7px}
.hero .kettle{position:absolute;left:640px;top:18px;width:330px;height:327px;border-radius:48% 48% 20% 20%;background:radial-gradient(circle at 40% 40%,#6c6c6c,#1a1a1a 70%)}
.hero .new{position:absolute;left:860px;top:40px;width:100px;height:100px;border-radius:50%;background:var(--blue);border:4px solid #fff;color:#fff;font-family:"Raleway",sans-serif;font-weight:800;font-size:30px;text-align:center;line-height:92px;transform:rotate(-12deg)}

/* categories */
.cats{top:511px;height:318px}
.cat{position:absolute;top:0;width:235px;height:318px;border:1px solid var(--line);background:#fff}
.cat h3{background:var(--orange);color:#fff;font-size:13px;font-weight:700;text-align:center;height:32px;padding-top:8px;text-transform:uppercase}
.cat .ph{height:100px;margin:0}
.cat ul{padding:16px 0 0 28px}
.cat li{font-size:12px;color:#555;height:32px}
.cat li::before{content:"";display:inline-block;width:14px;height:1px;background:#777;margin-right:14px;vertical-align:4px}
.totop{position:absolute;left:1150px;top:713px;width:38px;height:38px;background:var(--dark)}

/* section titles */
.stitle{position:absolute;height:40px}
.stitle::before{content:"";position:absolute;left:0;right:0;top:18px;height:4px;border-top:1px solid var(--orange);border-bottom:1px solid var(--orange)}
.stitle span{position:absolute;left:50%;transform:translateX(-50%) skewX(-15deg);top:4px;background:var(--label);color:#fff;font-family:"Raleway",sans-serif;font-weight:800;font-size:15px;padding:7px 26px;white-space:nowrap;text-transform:uppercase}
.stitle span b{display:inline-block;transform:skewX(15deg);font-weight:800}
.stitle .dots{position:absolute;left:50%;top:38px;transform:translateX(-50%);display:flex;gap:6px}
.stitle .dots i{width:18px;height:18px;border:1px solid #ccc;border-radius:50%;background:#fff}

/* product bits */
.pname{font-family:"Raleway",sans-serif;font-weight:700;font-size:11px;text-transform:uppercase;color:#222}
.price{color:var(--price);font-weight:700;font-size:15px}
.price s{color:#aaa;font-weight:400;font-size:10px;margin-left:4px}
.stars{color:#ccc;font-size:12px;letter-spacing:1px}
.stars.on{color:#f4b400}
.btn{display:inline-block;border:1px solid #bbb;font-size:9px;font-weight:700;padding:5px 9px;color:#333;text-transform:uppercase;background:#fff}

/* top sellers */
.tops{top:953px;height:470px}
.mini{position:absolute;width:320px;height:137px;border:3px solid var(--cardline);background:#fff}
.mini.hl{border-color:var(--orange)}
.mini .ph{position:absolute;left:14px;top:22px;width:110px;height:88px}
.mini .info{position:absolute;left:140px;top:22px}
.mini .info > *{margin-bottom:8px}
.feature{position:absolute;left:348px;top:0;width:320px;height:470px;border:3px solid var(--orange);background:#fff}
.feature .ph{position:absolute;left:24px;top:20px;width:266px;height:240px}
.feature .info{position:absolute;left:24px;top:268px;width:266px}
.feature p{font-size:11px;color:#666;line-height:1.45;margin:6px 0 10px}
.feature .actions{display:flex;gap:4px;margin-top:10px}
.feature .actions i{width:22px;height:22px;background:var(--dark)}

/* banners */
.banners{top:1467px;height:195px}
.banner{position:absolute;top:0;height:195px;color:#fff;font-family:"Raleway",sans-serif;text-align:center}
.b1{left:0;width:407px;background:linear-gradient(120deg,#5a5a5a,#2e2e2e)}
.b1 h3{position:absolute;left:0;right:0;top:52px;font-size:52px;font-weight:800;letter-spacing:2px}
.b1 p{position:absolute;left:0;right:0;top:118px;font-size:22px;font-weight:600}
.b2{left:433px;width:320px;background:linear-gradient(120deg,#b8b0a8,#6d6660)}
.b2 div{position:absolute;left:28px;top:70px;width:264px;height:56px;border:3px solid #fff;font-size:20px;font-weight:800;padding-top:12px}
.b3{left:780px;width:234px;background:var(--blue)}
.b3 .frame{position:absolute;left:10px;top:10px;right:10px;bottom:10px;border:2px solid #fff}
.b3 .gift{position:absolute;left:100px;top:28px}
.b3 h4{position:absolute;left:0;right:0;top:66px;font-size:16px;font-weight:700}
.b3 h3{position:absolute;left:0;right:0;top:88px;font-size:32px;font-weight:800}
.b3 p{position:absolute;left:0;right:0;top:138px;font-size:15px;font-weight:600}

/* featured + hot */
.feat{top:1800px;height:610px}
.fcard{position:absolute;left:0;width:320px;height:168px;border:3px solid var(--cardline);background:#fff}
.fcard .ph{position:absolute;left:14px;top:28px;width:110px;height:100px}
.fcard .info{position:absolute;left:140px;top:32px}
.fcard .info > *{margin-bottom:9px}
.pcard{position:absolute;width:152px;height:290px;border:1px solid var(--line);background:#fff}
.pcard .ph{position:absolute;left:16px;top:18px;width:118px;height:130px}
.pcard .info{position:absolute;left:16px;top:168px}
.pcard .info > *{margin-bottom:8px}

/* new products */
.newp{top:2550px;height:265px}
.ncard{position:absolute;top:0;width:156px;height:265px;border:1px solid var(--line);background:#fff}
.ncard .ph{position:absolute;left:16px;top:20px;width:122px;height:120px}
.ncard .info{position:absolute;left:12px;top:158px}
.ncard .info > *{margin-bottom:8px}

/* news */
.news{top:2963px;height:305px}
.post{position:absolute;top:0;width:305px}
.post .ph{height:165px;position:relative}
.post .date{position:absolute;right:0;bottom:0;background:var(--dark);color:#fff;font-size:10px;padding:4px 10px}
.post .date::before{content:"";position:absolute;left:-18px;top:0;border-style:solid;border-width:0 18px 22px 0;border-color:transparent var(--green) transparent transparent}
.post h3{font-size:16px;font-weight:700;color:#222;margin:14px 0 6px}
.post p{font-size:11px;color:#666;line-height:1.5;margin-bottom:14px}

/* brands */
.brands{top:3318px;height:100px;border-top:1px solid var(--line)}
.brands ul{position:absolute;left:93px;top:0;width:1014px;display:flex;justify-content:space-between}
.brands li{display:flex;align-items:center;gap:8px;font-family:"Raleway",sans-serif;font-weight:700;font-size:19px;color:#333;line-height:1;text-transform:uppercase;width:150px}
.brands li i{width:34px;height:34px;border-radius:50%;background:var(--orange);flex:none}

/* features band */
.perks{top:3451px;height:108px;background:var(--blue);color:#fff}
.perk{position:absolute;top:22px;width:250px;height:64px;border-left:1px solid rgba(255,255,255,.35);padding-left:80px}
.perk:first-child{border-left:none}
.perk svg{position:absolute;left:16px;top:8px}
.perk h4{font-size:12px;font-weight:800;text-transform:uppercase;margin:12px 0 4px}
.perk p{font-size:10px;opacity:.9}
.socials{display:flex;gap:8px;margin-top:6px}
.socials i{width:22px;height:22px;border:1px solid #fff;border-radius:50%}

/* footer */
.fnav{top:3559px;height:44px;background:#333}
.fnav ul{position:absolute;left:93px;top:15px;display:flex;gap:16px;font-size:10px;color:#ccc;text-transform:uppercase}
.footer{top:3603px;height:449px;background:var(--darker);color:#999}
.fcol{position:absolute;top:24px;width:230px}
.fcol h4{color:#fff;font-size:14px;font-weight:600;text-transform:uppercase;padding-bottom:14px;border-bottom:1px solid #3a3a3a;margin-bottom:18px}
.fcol p{font-size:11px;line-height:1.6;margin-bottom:14px}
.fcol h5{color:#fff;font-size:12px;font-weight:700;margin-bottom:6px}
.fcol li{font-size:11px;margin-bottom:22px}
.fcol input{width:230px;height:30px;border:none;background:#fff;font-size:11px;padding:0 10px;font-family:inherit}
.fcol .sub{display:inline-block;background:var(--blue);color:#fff;font-size:10px;font-weight:700;padding:6px 14px;margin:12px 0 22px;text-transform:uppercase}
.cards{display:flex;gap:8px}
.cards i{width:36px;height:22px;background:#ddd;border-radius:3px}
.copy{top:4052px;height:48px;background:#1c1c1c;color:#888;font-size:11px;text-align:center;padding-top:16px}
.copy b{color:var(--orange);font-weight:400}
</style>
</head>
<body>

<div class="sec topbar">
  <div class="left"><span>My account ▾</span><span>English ▾</span><span>Currency : USD ▾</span></div>
  <div class="right"><span>Email: hello@kitchennest-shop.com</span><span>Phone: (555) 0148 2260</span></div>
</div>

<header class="sec header">
  <div class="logo">Kitchen Nest</div>
  <div class="search">Search...
    <svg width="14" height="14" viewBox="0 0 14 14"><circle cx="6" cy="6" r="4.5" fill="none" stroke="#ddd" stroke-width="1.6"/><line x1="9.2" y1="9.2" x2="13" y2="13" stroke="#ddd" stroke-width="1.8"/></svg>
  </div>
</header>

<nav class="sec nav">
  <ul>
    <li class="active">Home</li><li>Gas Cooker</li><li>Pots</li><li>Kettles</li><li>Plates</li><li>Microwave</li><li>Dish Washer</li><li>Heat Extractor</li>
  </ul>
  <div class="cart">
    <svg width="20" height="20" viewBox="0 0 20 20"><path d="M1 3h3l2.5 10h10l2-7H5.5" fill="none" stroke="#222" stroke-width="1.8"/><circle cx="8" cy="17" r="1.6" fill="#222"/><circle cx="15" cy="17" r="1.6" fill="#222"/></svg>
    My Cart &nbsp;0 item
  </div>
</nav>

<section class="sec hero">
  <h1>Best Product</h1>
  <div class="tag">KITCHEN APPLIANCES</div>
  <div class="shop">Shop now</div>
  <div class="kettle" role="img" aria-label="Photo of a black stovetop whistling kettle"></div>
  <div class="new">NEW</div>
</section>

<section class="sec cats">
  <div class="cat" style="left:93px"><h3>Bowls and Plates</h3><div class="ph" role="img" aria-label="Photo of stacked ceramic bowls" style="background:linear-gradient(180deg,#ece9e4,#b9b3aa)"></div><ul><li>item1</li><li>item2</li><li>item3</li><li>item4</li></ul></div>
  <div class="cat" style="left:354px"><h3>Kettles</h3><div class="ph" role="img" aria-label="Photo of a kitchen shelf with kettles" style="background:linear-gradient(180deg,#9a8d80,#4f4640)"></div><ul><li>item1</li><li>item2</li><li>item3</li><li>item4</li></ul></div>
  <div class="cat" style="left:616px"><h3>Blender</h3><div class="ph" role="img" aria-label="Photo of a blender on a counter" style="background:linear-gradient(180deg,#d9d4cd,#8f877d)"></div><ul><li>item1</li><li>item2</li><li>item3</li><li>item4</li></ul></div>
  <div class="cat" style="left:874px"><h3>Cooker</h3><div class="ph" role="img" aria-label="Photo of a gas cooker hob" style="background:linear-gradient(180deg,#6f6f6f,#2c2c2c)"></div><ul><li>item1</li><li>item2</li><li>item3</li><li>item4</li></ul></div>
  <div class="totop" style="top:202px"><svg width="38" height="38" viewBox="0 0 38 38"><path d="M13 22l6-6 6 6" fill="none" stroke="#fff" stroke-width="2"/></svg></div>
</section>

<div class="stitle" style="top:868px;left:93px;width:1014px"><span><b>Top Sellers</b></span></div>

<section class="wrap tops" style="top:953px">
  <div class="mini hl" style="left:0;top:0"><div class="ph" role="img" aria-label="Photo of coloured cups" style="background:linear-gradient(90deg,#e9b3c8,#8fd0d3)"></div><div class="info"><div class="pname">Blouse</div><div class="price">$7.00<s>$20.00</s></div><div class="stars">★★★★★</div></div></div>
  <div class="mini" style="left:0;top:167px"><div class="ph" role="img" aria-label="Photo of orange mixing bowls" style="background:linear-gradient(180deg,#f7a35a,#d9661c)"></div><div class="info"><div class="pname">Cras Neque Metus</div><div class="price">$26.00</div><div class="stars">★★★★★</div></div></div>
  <div class="mini" style="left:0;top:333px"><div class="ph" role="img" aria-label="Photo of a steel kettle" style="background:linear-gradient(180deg,#cfcfcf,#6d6d6d)"></div><div class="info"><div class="pname">Faded Short</div><div class="price">$10.51<s>$20.00</s></div><div class="stars on">★★★★★</div></div></div>

  <div class="feature">
    <div class="ph" role="img" aria-label="Photo of four coloured drinking cups" style="background:linear-gradient(90deg,#ecb7cb,#f4e7a4,#93d4d6)"></div>
    <div class="info">
      <div class="pname">Blouse</div>
      <p>Faded short sleeves t-shirt with high neckline. Soft and stretchy material for a comfortable fit. Accessorize with a straw hat and you're ready for summer!</p>
      <div class="price">$7.00<s>$20.00</s></div>
      <div class="stars" style="margin-top:6px">★★★★★</div>
      <div class="actions"><span class="btn">Add to cart</span><i></i><i></i><i></i></div>
    </div>
  </div>

  <div class="mini" style="left:691px;top:0"><div class="ph" role="img" aria-label="Photo of a whisk" style="background:linear-gradient(180deg,#f1f1f1,#bdbdbd)"></div><div class="info"><div class="pname">Occaecati</div><div class="price">$10.50<s>$20.00</s></div><div class="stars">★★★★★</div></div></div>
  <div class="mini" style="left:691px;top:167px"><div class="ph" role="img" aria-label="Photo of an induction hob" style="background:linear-gradient(180deg,#4a4a4a,#111)"></div><div class="info"><div class="pname">Consequences</div><div class="price">$20.50<s>$25.00</s></div><div class="stars">★★★★★</div></div></div>
  <div class="mini" style="left:691px;top:333px"><div class="ph" role="img" aria-label="Photo of a rice cooker" style="background:linear-gradient(180deg,#f0ece6,#b8afa2)"></div><div class="info"><div class="pname">Rationally</div><div class="price">$20.51<s>$25.00</s></div><div class="stars">★★★★★</div></div></div>
</section>

<section class="wrap banners">
  <div class="banner b1" role="img" aria-label="Photo of blenders in a kitchen"><h3>BLEND</h3><p>LIKE NEVER BEFORE</p></div>
  <div class="banner b2" role="img" aria-label="Photo of a knife cutting vegetables"><div>KITCHEN KNIFE SETS</div></div>
  <div class="banner b3"><div class="frame"></div>
    <svg class="gift" width="34" height="32" viewBox="0 0 34 32"><rect x="3" y="11" width="28" height="19" fill="none" stroke="#fff" stroke-width="2"/><rect x="1" y="6" width="32" height="6" fill="none" stroke="#fff" stroke-width="2"/><line x1="17" y1="6" x2="17" y2="30" stroke="#fff" stroke-width="2"/></svg>
    <h4>CREATIVE STUFF</h4><h3>MEGA SALE</h3><p>from $20.00</p></div>
</section>

<div class="stitle" style="top:1705px;left:93px;width:320px"><span><b>Featured Products</b></span></div>
<div class="stitle" style="top:1705px;left:441px;width:666px"><span><b>Hot Sale</b></span><div class="dots"><i></i><i></i></div></div>

<section class="wrap feat">
  <div class="fcard" style="top:0"><div class="ph" role="img" aria-label="Photo of a steel kettle" style="background:linear-gradient(180deg,#d5d5d5,#6b6b6b)"></div><div class="info"><div class="pname">Faded Short</div><div class="price">$10.51<s>$20.00</s></div><div class="stars on">★★★★★</div><span class="btn">Add to cart</span></div></div>
  <div class="fcard" style="top:204px"><div class="ph" role="img" aria-label="Photo of coloured cups" style="background:linear-gradient(90deg,#e9b3c8,#8fd0d3)"></div><div class="info"><div class="pname">Blouse</div><div class="price">$7.00<s>$20.00</s></div><div class="stars">★★★★★</div><span class="btn">Add to cart</span></div></div>
  <div class="fcard" style="top:404px"><div class="ph" role="img" aria-label="Photo of orange mixing bowls" style="background:linear-gradient(180deg,#f7a35a,#d9661c)"></div><div class="info"><div class="pname">Cras Neque Metus</div><div class="price">$26.00</div><div class="stars">★★★★★</div><span class="btn">Add to cart</span></div></div>

  <div class="pcard" style="left:348px;top:0"><div class="ph" role="img" aria-label="Photo of a corkscrew" style="background:linear-gradient(180deg,#f2f2f2,#b4a6a0)"></div><div class="info"><div class="pname">Nunc Facilisis</div><div class="price">$330.00<s>$400.00</s></div><div class="stars on">★★★★☆</div><span class="btn">Add to cart</span></div></div>
  <div class="pcard" style="left:520px;top:0"><div class="ph" role="img" aria-label="Photo of coloured silicone spatulas" style="background:linear-gradient(90deg,#4aa3df,#e74c3c,#f1c40f,#2ecc71)"></div><div class="info"><div class="pname">Accumsan Elit</div><div class="price">$180.00<s>$200.00</s></div><div class="stars">★★★★★</div><span class="btn">Add to cart</span></div></div>
  <div class="pcard" style="left:692px;top:0"><div class="ph" role="img" aria-label="Photo of an electric kettle" style="background:linear-gradient(180deg,#f3efe9,#b9b0a3)"></div><div class="info"><div class="pname">Rationally</div><div class="price">$20.51<s>$25.00</s></div><div class="stars">★★★★★</div><span class="btn">Add to cart</span></div></div>
  <div class="pcard" style="left:862px;top:0"><div class="ph" role="img" aria-label="Photo of a rice cooker" style="background:linear-gradient(180deg,#f6f6f6,#bcbcbc)"></div><div class="info"><div class="pname">Rationally</div><div class="price">$20.51<s>$25.00</s></div><div class="stars">★★★★★</div><span class="btn">Add to cart</span></div></div>

  <div class="pcard" style="left:348px;top:318px"><div class="ph" role="img" aria-label="Photo of a black kettle" style="background:linear-gradient(180deg,#5a5a5a,#111)"></div><div class="info"><div class="pname">Primis in Faucibus</div><div class="price">$228.00<s>$250.00</s></div><div class="stars">★★★★★</div><span class="btn">Add to cart</span></div></div>
  <div class="pcard" style="left:520px;top:318px"><div class="ph" role="img" aria-label="Photo of a red kettle" style="background:linear-gradient(180deg,#e0403a,#8e1612)"></div><div class="info"><div class="pname">Voluptas Nulla</div><div class="price">$30.99<s>$40.00</s></div><div class="stars">★★★★★</div><span class="btn">Add to cart</span></div></div>
  <div class="pcard" style="left:692px;top:318px"><div class="ph" role="img" aria-label="Photo of an induction hob" style="background:linear-gradient(180deg,#4a4a4a,#111)"></div><div class="info"><div class="pname">Consequences</div><div class="price">$20.50<s>$25.00</s></div><div class="stars">★★★★★</div><span class="btn">Add to cart</span></div></div>
</section>

<div class="stitle" style="top:2445px;left:93px;width:1014px"><span><b>New Products</b></span><div class="dots"><i></i><i></i></div></div>

<section class="wrap newp">
  <div class="ncard" style="left:0"><div class="ph" role="img" aria-label="Photo of an induction hob" style="background:linear-gradient(180deg,#4a4a4a,#111)"></div><div class="info"><div class="pname">Etiam Gravida</div><div class="price">$300.00</div><span class="btn">Add to cart</span></div></div>
  <div class="ncard" style="left:171px"><div class="ph" role="img" aria-label="Photo of a vacuum cleaner" style="background:linear-gradient(180deg,#6d5a7a,#2a2230)"></div><div class="info"><div class="pname">Aliquam Consequat</div><div class="price">$280.00</div><span class="btn">Add to cart</span></div></div>
  <div class="ncard" style="left:343px"><div class="ph" role="img" aria-label="Photo of a lunch box" style="background:linear-gradient(180deg,#f08a3a,#e4e1dc)"></div><div class="info"><div class="pname">Donec Non Est</div><div class="price">$220.00</div><span class="btn">Add to cart</span></div></div>
  <div class="ncard" style="left:514px"><div class="ph" role="img" aria-label="Photo of a corkscrew" style="background:linear-gradient(180deg,#f2f2f2,#b4a6a0)"></div><div class="info"><div class="pname">Nunc Facilisis</div><div class="price">$330.00<s>$400</s></div><div class="stars on">★★★★☆</div><span class="btn">Add to cart</span></div></div>
  <div class="ncard" style="left:686px"><div class="ph" role="img" aria-label="Photo of a black kettle" style="background:linear-gradient(180deg,#5a5a5a,#111)"></div><div class="info"><div class="pname">Primis in Faucibus</div><div class="price">$228.00<s>$250</s></div><span class="btn">Add to cart</span></div></div>
  <div class="ncard" style="left:858px"><div class="ph" role="img" aria-label="Photo of coloured spatulas" style="background:linear-gradient(90deg,#4aa3df,#e74c3c,#f1c40f,#2ecc71)"></div><div class="info"><div class="pname">Accumsan Elit</div><div class="price">$180.00<s>$200</s></div><span class="btn">Add to cart</span></div></div>
</section>

<div class="stitle" style="top:2868px;left:93px;width:1014px"><span><b>Latest News</b></span><div class="dots"><i></i><i></i></div></div>

<section class="wrap news">
  <article class="post" style="left:0"><div class="ph" role="img" aria-label="Photo of vegetables tossed in a wok" style="background:linear-gradient(135deg,#c9a24a,#4c3a1f)"><span class="date">12 July</span></div><h3>New kitchen utensils Arrived</h3><p>Lorem Ipsum is simply dummy text of the printing and typesetting industry. Lorem Ipsum has been the industry's standard.</p><span class="btn">Read more</span></article>
  <article class="post" style="left:354px"><div class="ph" role="img" aria-label="Photo of a bright kitchen counter" style="background:linear-gradient(135deg,#e9e2d8,#9a7d62)"><span class="date">12 July</span></div><h3>Answers to about Our Products</h3><p>Lorem Ipsum is simply dummy text of the printing and typesetting industry. Lorem Ipsum has been the industry's standard.</p><span class="btn">Read more</span></article>
  <article class="post" style="left:709px"><div class="ph" role="img" aria-label="Photo of hands chopping mushrooms" style="background:linear-gradient(135deg,#efe6d9,#b85b3a)"><span class="date">12 July</span></div><h3>What is new</h3><p>Lorem Ipsum is simply dummy text of the printing and typesetting industry. Lorem Ipsum has been the industry's standard.</p><span class="btn">Read more</span></article>
</section>

<section class="sec brands">
  <ul style="top:30px">
    <li><i style="background:#3aa58a"></i>Logo<br>Brand</li>
    <li><i style="background:var(--red)"></i>Logo<br>Brand</li>
    <li><i style="background:#2a8fbf"></i>Logo<br>Brand</li>
    <li><i style="background:#f39c12"></i>Logo<br>Brand</li>
    <li><i style="background:#f39c12"></i>Logo<br>Brand</li>
  </ul>
</section>

<section class="sec perks">
  <div class="wrap" style="top:0;height:108px">
    <div class="perk" style="left:0">
      <svg width="48" height="48" viewBox="0 0 48 48"><circle cx="24" cy="24" r="22" fill="none" stroke="#fff" stroke-width="1.5"/><path d="M13 18h14v11H13zM27 22h5l3 4v3h-8" fill="none" stroke="#fff" stroke-width="1.6"/><circle cx="18" cy="31" r="2" fill="#fff"/><circle cx="31" cy="31" r="2" fill="#fff"/></svg>
      <h4>Free Shipping</h4><p>On order over $500.00</p></div>
    <div class="perk" style="left:254px">
      <svg width="48" height="48" viewBox="0 0 48 48"><circle cx="24" cy="24" r="22" fill="none" stroke="#fff" stroke-width="1.5"/><path d="M16 20h14a5 5 0 010 10H20M16 20l4-4M16 20l4 4" fill="none" stroke="#fff" stroke-width="1.6"/></svg>
      <h4>Free Return</h4><p>Free returns within 30 days</p></div>
    <div class="perk" style="left:508px">
      <svg width="48" height="48" viewBox="0 0 48 48"><circle cx="24" cy="24" r="22" fill="none" stroke="#fff" stroke-width="1.5"/><rect x="15" y="16" width="18" height="16" fill="none" stroke="#fff" stroke-width="1.6"/><line x1="15" y1="21" x2="33" y2="21" stroke="#fff" stroke-width="1.6"/></svg>
      <h4>Daily Updates</h4><p>Check out store for latest</p></div>
    <div class="perk" style="left:762px">
      <svg width="48" height="48" viewBox="0 0 48 48"><circle cx="24" cy="24" r="22" fill="none" stroke="#fff" stroke-width="1.5"/><path d="M17 15l4 0 2 6-3 2a12 12 0 006 6l2-3 6 2v4a2 2 0 01-2 2A18 18 0 0115 17a2 2 0 012-2z" fill="none" stroke="#fff" stroke-width="1.6"/></svg>
      <h4>Support 24/7</h4><p>Phone: (555) 0148 2260</p></div>
  </div>
</section>

<nav class="sec fnav"><ul><li>Home</li><li>Specials</li><li>About Us</li><li>Advanced Search</li><li>Search Terms</li></ul>
  <div class="socials" style="position:absolute;left:960px;top:-34px"><i></i><i></i><i></i><i></i><i></i></div>
</nav>

<footer class="sec footer">
  <div class="fcol" style="left:93px">
    <h4>About Us</h4>
    <p>Lorem ipsum dolor sit amet, consectetur adipiscing elit, sed diam nonummy nibh euismod tincidunt.</p>
    <h5>Adress Office</h5><p>Address: 1234 Maple Street, Springfield, CA 00000, USA</p>
    <h5>Phone Number</h5><p>(555) 0148 2260<br>(555) 0148 2261</p>
    <h5>Email Adress</h5><p>hello@kitchennest-shop.com</p>
  </div>
  <div class="fcol" style="left:350px">
    <h4>Latest Tweets</h4>
    <h5>Lorem ipsum ghometit</h5><p>Lorem ipsum dolor sit amet aliquam erat volutpat.</p>
    <h5>Lorem ipsum ghometit</h5><p>Lorem ipsum dolor sit amet aliquam erat volutpat.</p>
  </div>
  <div class="fcol" style="left:615px">
    <h4>My Account</h4>
    <ul><li>My Orders</li><li>My Credit Slips</li><li>My Addresses</li><li>My Personal Info</li><li>Advanced Search</li></ul>
  </div>
  <div class="fcol" style="left:877px">
    <h4>Newsletter</h4>
    <p>Subscribe to our newsletter to stay up to date with new arrivals and special offers.</p>
    <input type="text" value="Enter your e-mail" aria-label="Email address">
    <span class="sub">Subscribe</span>
    <div class="cards"><i></i><i></i><i></i><i></i><i></i></div>
  </div>
</footer>

<div class="sec copy">Copyright © <b>KitchenNest</b>. All Rights Reserved</div>

</body>
</html>
```